Brightford Lingua Partners, LLC

We need a business card that includes information about our business and conveys a reliable business that provides document translation services and interpreters for a variety of corporate and individual clients. We want to come across as professional, reliable, yet approachable. It should include the following on one side:

ESL / ENL Language Classes, Private Lessons, and Online Tutors
PALQE Training and Testing
Translating & Interpreting Services
Contact us about Over-the-Phone Interpreting in over 200 languages
24/7/365
www.brightfordlingua.example

The other side should include (555) 481-3062

Marla Quennick, President
412 Garvin Ave., Ste. 209
Indianapolis, IN 46999
Updates

Please add USA as part of the address. Also, please add mrqquennick@brightfordlinguapartners.example as the e-mail address. Thank you.

Target Market(s)

Business professionals, their families, the international community

Industry/Entity Type

Business

Contact Information for Business Card

24/7/365
www.brightfordlingua.example

(555) 481-3062

Marla Quennick, President
412 Garvin Ave., Ste. 209
Indianapolis, IN 46999
USA

Font styles to use
Sans Serif

Colors

Designer to choose colors to be used in the design.

Requirements
Must have
• See project description
• e-mail address and web address
• Phone number
Nice to have
• a globe
• physical address
Should not have
• Should not have the same color scheme as other agencies in our market in Indiana unless it is blue and black. No purple or yellow.

```html
<!DOCTYPE html>
<html lang="en">
<head>
<meta charset="utf-8">
<title>Brightford Lingua Partners — Business Card</title>
<link rel="stylesheet" href="https://fonts.googleapis.com/css2?family=Questrial&family=Michroma&family=Open+Sans:ital,wght@1,400&family=Cabin:wght@500&display=swap">
<style>
  :root {
    --stage: #e9ebee;
    --paper: #ffffff;
    --ink: #141414;
    --brand-blue: #1f8fd8;
    --band-blue: #2399dc;
    --band-blue-light: #4fb6ea;
    --band-mid: #1b7fc6;
    --band-deep: #155fa8;
    --band-navy: #0f4785;
    --map-grey: #e4e5e7;
    --rule: #9cc8ea;
  }
  * { box-sizing: border-box; margin: 0; padding: 0; }
  html, body { width: 1200px; height: 800px; overflow: hidden; }
  body {
    background: var(--stage);
    display: flex; align-items: center; justify-content: center; gap: 40px;
    font-family: "Questrial", sans-serif; color: var(--ink);
  }
  .card {
    position: relative; width: 540px; height: 310px;
    background: var(--paper); border-radius: 14px; overflow: hidden;
    box-shadow: 0 6px 18px rgba(0,0,0,.18);
  }

  /* wordmark */
  .wordmark { position: absolute; display: flex; align-items: center; gap: 12px; }
  .wordmark-dot { width: 70px; height: 70px; border-radius: 50%; background: var(--brand-blue); flex: none; }
  .wordmark-name {
    font-family: "Cabin", sans-serif; font-weight: 500; color: var(--ink);
    font-size: 25px; line-height: 1.0;
  }

  /* front */
  .front-map {
    position: absolute; left: 0; top: 0; width: 150px; height: 100%;
    background: linear-gradient(160deg, #eeeff1, var(--map-grey));
  }
  .front .wordmark { left: 168px; top: 22px; }
  .holder { position: absolute; right: 26px; top: 110px; text-align: right; }
  .holder-name {
    font-family: "Michroma", sans-serif; color: var(--brand-blue);
    font-size: 14px; letter-spacing: 3px; font-weight: 700;
  }
  .holder-title { font-size: 17px; margin-top: 4px; letter-spacing: 1px; }
  .address-band {
    position: absolute; left: 150px; right: 0; top: 162px; height: 76px;
    background: linear-gradient(120deg, var(--band-blue-light), var(--band-blue) 60%, #1a83cf);
    color: #fff; text-align: center; padding-top: 7px;
    font-size: 17px; line-height: 1.25; letter-spacing: 1.5px;
  }
  .phone {
    position: absolute; left: 150px; right: 0; top: 244px;
    text-align: center; color: var(--brand-blue); font-size: 26px; letter-spacing: 1px; line-height: 1.1;
  }
  .email {
    position: absolute; left: 150px; right: 0; top: 280px;
    text-align: center; color: var(--ink); font-size: 12.5px; letter-spacing: .3px;
  }

  /* back */
  .back .wordmark { left: 24px; top: 40px; }
  .back-rule { position: absolute; left: 256px; top: 40px; width: 1px; height: 130px; background: var(--rule); }
  .service-list { position: absolute; left: 270px; right: 0; top: 54px; list-style: none; }
  .service {
    color: #fff; font-family: "Open Sans", sans-serif; font-style: italic;
    font-size: 12.5px; letter-spacing: .6px; padding: 6px 12px; margin-bottom: 4px; line-height: 1.3;
    white-space: nowrap;
  }
  .service--light { background: linear-gradient(100deg, var(--band-blue-light), var(--band-blue)); }
  .service--mid { background: linear-gradient(100deg, var(--band-blue), var(--band-mid)); }
  .service--deep { background: linear-gradient(100deg, var(--band-deep), var(--band-navy)); }
  .contact-line {
    position: absolute; left: 24px; right: 24px; top: 190px;
    color: var(--brand-blue); font-size: 14px; letter-spacing: .6px; white-space: nowrap;
  }
  .availability {
    position: absolute; left: 0; right: 0; top: 218px; text-align: center;
    color: var(--brand-blue); font-size: 30px; letter-spacing: 2px;
  }
  .website {
    position: absolute; left: 0; right: 0; top: 266px; text-align: center;
    color: var(--ink); font-size: 15px; letter-spacing: 1px;
  }
</style>
</head>
<body>
  <section class="card front" aria-label="Card front">
    <div class="front-map" role="img" aria-label="Street map showing the office location"></div>
    <div class="wordmark">
      <span class="wordmark-dot"></span>
      <span class="wordmark-name">Brightford<br>Lingua<br>Partners, LLC</span>
    </div>
    <div class="holder">
      <p class="holder-name">Marla Quennick</p>
      <p class="holder-title">President</p>
    </div>
    <div class="address-band">
      412 Garvin Ave., Ste. 209<br>
      Indianapolis, IN 46999<br>
      USA
    </div>
    <p class="phone">(555) 481-3062</p>
    <p class="email">mrqquennick@brightfordlinguapartners.example</p>
  </section>

  <section class="card back" aria-label="Card back">
    <div class="wordmark">
      <span class="wordmark-dot"></span>
      <span class="wordmark-name">Brightford<br>Lingua<br>Partners, LLC</span>
    </div>
    <div class="back-rule"></div>
    <ul class="service-list">
      <li class="service service--light">ESL / ENL Language Classes</li>
      <li class="service service--mid">Private Lessons &amp; Online Tutors<br>PALQE Training and Testing</li>
      <li class="service service--deep">Translating &amp; Interpreting Services</li>
    </ul>
    <p class="contact-line">Contact us about Over-the-Phone Interpreting in over 200 languages</p>
    <p class="availability">24x7x365</p>
    <p class="website">www.brightfordlingua.example</p>
  </section>
</body>
</html>
```